Simple Banners for several sites

I'm looking for banners in the following formats for the sites listed bellow:

* Leaderboard
* Wide Skyscraper
* Skyscaper
* Square Button
* Micro bar
* Full banner
* Half Banner
* Medium Rectangle

The websites:
* http://factheap.vornel.com/
* http://pagtrove.com/
* http://netolumba.com/

I would like to get 1 sets of banners for each website, and I'ld like you to submit each set/site independently.

```html
<!DOCTYPE html>
<html lang="pt">
<head>
<meta charset="utf-8">
<title>Netolumba – banner set</title>
<link rel="stylesheet" href="https://fonts.googleapis.com/css2?family=Source+Sans+3:wght@400;600;700&display=swap">
<style>
:root{
  --page:#1c1c1c;
  --panel:#474747;
  --panel-shade:#3f3f3f;
  --red:#a80a1d;
  --red-light:#c10f26;
  --red-dark:#8a0616;
  --white:#ffffff;
  --muted:#d8d8d8;
}
*{box-sizing:border-box;margin:0;padding:0}
html,body{width:1200px;height:883px;overflow:hidden;background:var(--page)}
body{font-family:"Source Sans 3",sans-serif;color:var(--white)}
.stage{position:absolute;left:0;top:0;width:1240px;height:912px;transform:scale(.9677);transform-origin:0 0;
  background:radial-gradient(ellipse at 50% 40%,#2b2b2b 0%,#1a1a1a 70%,#121212 100%)}
.size-label{position:absolute;font-size:14px;color:var(--muted);transform:translateX(-50%);letter-spacing:-.2px}
.banner{position:absolute;overflow:hidden;
  background:linear-gradient(112deg,var(--panel) 0 38%,var(--panel-shade) 38% 62%,var(--panel) 62%)}
.brand{position:absolute;background:var(--red);display:flex;align-items:center;justify-content:center;
  font-weight:700;letter-spacing:-.5px;box-shadow:0 2px 0 rgba(0,0,0,.25)}
.heading{position:absolute;font-weight:600;text-align:center;line-height:1;letter-spacing:-.6px}
.badge{position:absolute;width:var(--d);height:var(--d);margin:calc(var(--d)/-2) 0 0 calc(var(--d)/-2);
  border-radius:50%;background:var(--red);display:flex;flex-direction:column;align-items:center;justify-content:center;
  font-size:calc(var(--d)*.2);font-weight:600;letter-spacing:-.5px;line-height:1;box-shadow:0 0 0 1px rgba(0,0,0,.08)}
.badge svg{width:calc(var(--d)*.36);height:calc(var(--d)*.36);margin-bottom:calc(var(--d)*.04)}
.badge.small-label{font-size:calc(var(--d)*.165)}
.cta{position:absolute;display:flex;background:linear-gradient(var(--red-light),var(--red));border-radius:2px;
  box-shadow:0 2px 3px rgba(0,0,0,.35)}
.cta-label{flex:1;display:flex;align-items:center;justify-content:center;font-weight:400}
.cta-arrow{width:28%;display:flex;align-items:center;justify-content:center;background:var(--red-dark)}
.cta-arrow svg{width:38%;height:38%}
.site-url{position:absolute;color:var(--muted);text-align:center;transform:translateX(-50%);white-space:nowrap}
.site-url b{color:var(--white);font-weight:700}
.topic-bar{position:absolute;left:0;right:0;bottom:0;height:30px;background:var(--red);display:flex;
  align-items:center;justify-content:center;gap:9px;font-size:13px;font-weight:600;letter-spacing:-.3px}
.topic-bar span{display:flex;align-items:center;gap:3px}
.topic-bar svg{width:16px;height:16px}
</style>
</head>
<body>
<svg width="0" height="0" style="position:absolute" aria-hidden="true">
  <defs>
    <symbol id="icon-idea" viewBox="0 0 32 32">
      <g stroke="#fff" stroke-linecap="round" fill="none">
        <circle cx="16" cy="14" r="7.5" stroke-width="2.4"/>
        <path d="M16 9.5v5.5" stroke-width="2.6"/>
        <path d="M16 2v2.5M6 5.5l1.8 1.8M26 5.5l-1.8 1.8M2.5 14h2.5M27 14h2.5" stroke-width="1.6"/>
      </g>
      <circle cx="16" cy="17.8" r="1.4" fill="#fff"/>
      <rect x="12.5" y="22.5" width="7" height="5.5" rx="1" fill="#fff"/>
    </symbol>
    <symbol id="icon-tutorial" viewBox="0 0 32 32">
      <rect x="3" y="4" width="26" height="18" rx="1.5" fill="#fff"/>
      <rect x="5.5" y="6.5" width="21" height="11" fill="#a80a1d"/>
      <g fill="none" stroke="#fff" stroke-width="1">
        <rect x="8" y="8.5" width="4" height="4"/><rect x="14" y="8.5" width="4" height="4"/><rect x="20" y="8.5" width="4" height="4"/>
        <path d="M8 14.5h4M14 14.5h4M20 14.5h4"/>
      </g>
      <path d="M13 22h6l1.5 5h-9z" fill="#fff"/>
      <rect x="9" y="27" width="14" height="2" rx="1" fill="#fff"/>
    </symbol>
    <symbol id="icon-tech" viewBox="0 0 32 32">
      <g fill="none" stroke="#fff">
        <circle cx="12" cy="11" r="5" stroke-width="3.5"/>
        <circle cx="12" cy="11" r="8" stroke-width="3" stroke-dasharray="3.2 3.1"/>
        <circle cx="23" cy="20" r="3.3" stroke-width="2.6"/>
        <circle cx="23" cy="20" r="5.6" stroke-width="2.4" stroke-dasharray="2.4 2.2"/>
        <circle cx="10.5" cy="25" r="2.6" stroke-width="2.2"/>
        <circle cx="10.5" cy="25" r="4.5" stroke-width="2" stroke-dasharray="2 1.9"/>
      </g>
    </symbol>
    <symbol id="icon-chevrons" viewBox="0 0 20 20">
      <path d="M3 4l6 6-6 6M10 4l6 6-6 6" fill="none" stroke="#fff" stroke-width="3" stroke-linecap="round" stroke-linejoin="round"/>
    </symbol>
  </defs>
</svg>

<main class="stage">
  <!-- Wide skyscraper -->
  <div class="size-label" style="left:182px;top:151px">160x600</div>
  <section class="banner" style="left:105px;top:179px;width:160px;height:600px">
    <div class="brand" style="left:0;top:0;width:160px;height:66px;font-size:25px">Netolumba</div>
    <div class="heading" style="left:0;top:105px;width:160px;font-size:19px">Desenvolvimento</div>
    <div class="heading" style="left:0;top:130px;width:160px;font-size:28px">Web</div>
    <div class="badge" style="--d:100px;left:81px;top:235px"><svg><use href="#icon-idea"/></svg>idéias</div>
    <div class="badge" style="--d:100px;left:81px;top:347px"><svg><use href="#icon-tutorial"/></svg>tutoriais</div>
    <div class="badge small-label" style="--d:100px;left:79px;top:455px"><svg><use href="#icon-tech"/></svg>tecnologias</div>
    <div class="cta" style="left:7px;top:542px;width:145px;height:44px">
      <span class="cta-label" style="font-size:18px">Continuar</span>
      <span class="cta-arrow"><svg><use href="#icon-chevrons"/></svg></span>
    </div>
  </section>

  <!-- Skyscraper -->
  <div class="size-label" style="left:351px;top:151px">120x600</div>
  <section class="banner" style="left:291px;top:179px;width:120px;height:600px">
    <div class="brand" style="left:0;top:0;width:120px;height:64px;font-size:21px">Netolumba</div>
    <div class="heading" style="left:0;top:105px;width:120px;font-size:14.5px">Desenvolvimento</div>
    <div class="heading" style="left:0;top:127px;width:120px;font-size:28px">Web</div>
    <div class="badge" style="--d:100px;left:61px;top:230px"><svg><use href="#icon-idea"/></svg>idéias</div>
    <div class="badge" style="--d:98px;left:61px;top:341px"><svg><use href="#icon-tutorial"/></svg>tutoriais</div>
    <div class="badge small-label" style="--d:98px;left:59px;top:449px"><svg><use href="#icon-tech"/></svg>tecnologias</div>
    <div class="cta" style="left:3px;top:542px;width:115px;height:34px">
      <span class="cta-label" style="font-size:15px">Continuar</span>
      <span class="cta-arrow"><svg><use href="#icon-chevrons"/></svg></span>
    </div>
    <div class="site-url" style="left:60px;top:583px;font-size:11px">www.netolumba.com</div>
  </section>

  <!-- Medium rectangle -->
  <div class="size-label" style="left:591px;top:287px">300x250</div>
  <section class="banner" style="left:441px;top:316px;width:300px;height:250px">
    <div class="brand" style="left:63px;top:0;width:171px;height:58px;font-size:26px">Netolumba</div>
    <div class="heading" style="left:0;top:81px;width:290px;font-size:26px">Desenvolvimento Web</div>
    <div class="badge" style="--d:98px;left:62px;top:204px"><svg><use href="#icon-idea"/></svg>idéias</div>
    <div class="badge small-label" style="--d:98px;left:147px;top:182px"><svg><use href="#icon-tech"/></svg>tecnologias</div>
    <div class="badge" style="--d:98px;left:236px;top:200px"><svg><use href="#icon-tutorial"/></svg>tutoriais</div>
  </section>

  <!-- Full banner -->
  <div class="size-label" style="left:669px;top:576px">468x60</div>
  <section class="banner" style="left:441px;top:599px;width:468px;height:60px">
    <div class="heading" style="left:14px;top:13px;font-size:13px;text-align:left">Desenvolvimento</div>
    <div class="heading" style="left:43px;top:32px;font-size:16px;text-align:left">Web</div>
    <div class="badge" style="--d:62px;left:166px;top:31px"><svg><use href="#icon-idea"/></svg>idéias</div>
    <div class="badge" style="--d:62px;left:227px;top:31px"><svg><use href="#icon-tutorial"/></svg>tutoriais</div>
    <div class="badge small-label" style="--d:62px;left:287px;top:31px"><svg><use href="#icon-tech"/></svg>tecnologias</div>
    <div class="cta" style="left:363px;top:11px;width:93px;height:28px">
      <span class="cta-label" style="font-size:12px">Continuar</span>
      <span class="cta-arrow"><svg><use href="#icon-chevrons"/></svg></span>
    </div>
    <div class="site-url" style="left:409px;top:43px;font-size:8px">www.<b>netolumba</b>.com</div>
  </section>

  <!-- Half banner -->
  <div class="size-label" style="left:1051px;top:576px">234x60</div>
  <section class="banner" style="left:935px;top:599px;width:234px;height:60px">
    <div class="heading" style="left:0;top:6px;width:234px;font-size:20px">Desenvolvimento Web</div>
    <div class="topic-bar">
      <span><svg><use href="#icon-idea"/></svg>idéias</span>
      <span><svg><use href="#icon-tech"/></svg>tecnologias</span>
      <span><svg><use href="#icon-tutorial"/></svg>tutoriais</span>
    </div>
  </section>

  <!-- Leaderboard -->
  <section class="banner" style="left:441px;top:689px;width:728px;height:90px">
    <div class="heading" style="left:22px;top:20px;font-size:20px;text-align:left">Desenvolvimento</div>
    <div class="heading" style="left:67px;top:48px;font-size:26px;text-align:left">Web</div>
    <div class="badge" style="--d:98px;left:258px;top:55px"><svg><use href="#icon-idea"/></svg>idéias</div>
    <div class="badge" style="--d:98px;left:352px;top:49px"><svg><use href="#icon-tutorial"/></svg>tutoriais</div>
    <div class="badge small-label" style="--d:98px;left:445px;top:47px"><svg><use href="#icon-tech"/></svg>tecnologias</div>
    <div class="cta" style="left:565px;top:16px;width:145px;height:44px">
      <span class="cta-label" style="font-size:18px">Continuar</span>
      <span class="cta-arrow"><svg><use href="#icon-chevrons"/></svg></span>
    </div>
    <div class="site-url" style="left:636px;top:64px;font-size:14px">www.<b>netolumba</b>.com</div>
  </section>
  <div class="size-label" style="left:792px;top:796px">728x90</div>
</main>
</body>
</html>
```